IT Company based on Biology Business Needs a Business Card Design

We need a business card design for a new company called 'Lumen CELL'. We develop the machine learning solutions especially focused on deep learning algorithms for biology industry. Our initial product is a vision detection on biological images to help doctors diagnose the symptoms. We would like to see designs that use the color green.

Industry/Entity Type

Business

```html
<!DOCTYPE html>
<html lang="en">
<head>
<meta charset="utf-8">
<title>Lumen CELL — Business Card</title>
<link href="https://fonts.googleapis.com/css2?family=Lato:ital,wght@0,400;0,700;1,400&display=swap" rel="stylesheet">
<style>
  :root {
    --backdrop: #e6e8e6;
    --card-white: #f4f5f4;
    --card-black: #151515;
    --brand-green: #4caf46;
    --brand-green-deep: #3e9b39;
    --bar-white: #f7f7f7;
    --text-dark: #2a2a2a;
    --text-light: #ffffff;
    --text-muted: #cfcfcf;
  }
  * { box-sizing: border-box; margin: 0; padding: 0; }
  html, body { width: 1200px; height: 800px; overflow: hidden; }
  body {
    background: var(--backdrop);
    font-family: "Lato", sans-serif;
    position: relative;
  }
  .card {
    position: absolute;
    width: 560px;
    height: 320px;
    box-shadow: 0 10px 24px rgba(0,0,0,0.18);
    display: flex;
    overflow: hidden;
  }
  /* Front: brand side */
  .card-front { left: 580px; top: 70px; background: var(--card-white); }
  .card-front .brand-area {
    flex: 0 0 62%;
    display: flex; align-items: center; justify-content: center;
  }
  .card-front .green-band { flex: 1; background: var(--brand-green); }

  .wordmark {
    display: flex; align-items: center; gap: 12px;
    color: var(--brand-green);
    font-weight: 700;
    font-size: 38px;
    letter-spacing: 0.5px;
  }
  .wordmark .dot {
    width: 18px; height: 18px; border-radius: 50%;
    background: var(--brand-green);
  }

  /* Back: contact side */
  .card-back { left: 80px; top: 410px; background: var(--card-white); }
  .contact-panel {
    flex: 0 0 58%;
    background: var(--card-black);
    padding: 32px 0 0 34px;
  }
  .person-name {
    color: var(--text-light);
    font-size: 21px; font-weight: 400; letter-spacing: 1px;
    text-transform: uppercase;
  }
  .person-title {
    color: var(--text-muted);
    font-style: italic; font-size: 15px;
    margin-top: 2px;
  }
  .contact-list { list-style: none; margin-top: 22px; }
  .contact-row {
    display: flex; height: 44px; margin-bottom: 12px;
  }
  .contact-icon {
    flex: 0 0 58px;
    background: var(--brand-green);
    display: flex; align-items: center; justify-content: center;
  }
  .contact-icon svg { width: 24px; height: 24px; }
  .contact-text {
    flex: 1;
    background: var(--bar-white);
    color: var(--text-dark);
    font-size: 14px; letter-spacing: 0.5px;
    display: flex; flex-direction: column; justify-content: center;
    padding-left: 26px;
    line-height: 1.15;
    margin-right: -28px;
    position: relative; z-index: 1;
  }
  .brand-panel {
    flex: 1;
    display: flex; align-items: center; justify-content: center;
    padding-left: 20px;
  }
  .brand-panel .wordmark { font-size: 30px; gap: 10px; }
  .brand-panel .wordmark .dot { width: 14px; height: 14px; }
</style>
</head>
<body>

  <section class="card card-front" aria-label="Business card front">
    <div class="brand-area">
      <div class="wordmark"><span class="dot"></span>Lumen CELL</div>
    </div>
    <div class="green-band"></div>
  </section>

  <section class="card card-back" aria-label="Business card back">
    <div class="contact-panel">
      <h1 class="person-name">Marta Ellis</h1>
      <p class="person-title">Chief Executive</p>
      <ul class="contact-list">
        <li class="contact-row">
          <span class="contact-icon">
            <svg viewBox="0 0 24 24" fill="none" stroke="#fff" stroke-width="1.5">
              <rect x="2" y="2" width="20" height="20" rx="3"/>
              <path d="M8 6.5c-1 .8-1.3 2.2-.4 4 1.2 2.5 3.2 4.6 5.6 5.8 1.7.9 3 .6 3.8-.4l-2-2-1.5 1c-1.6-.8-2.9-2.1-3.7-3.7l1-1.5z" fill="#fff" stroke="none"/>
            </svg>
          </span>
          <span class="contact-text"><span>555 204 318</span><span>555 204 318</span></span>
        </li>
        <li class="contact-row">
          <span class="contact-icon">
            <svg viewBox="0 0 24 24" fill="none" stroke="#fff" stroke-width="1.5">
              <rect x="2" y="2" width="20" height="20" rx="3"/>
              <rect x="6" y="8" width="12" height="8" fill="#fff" stroke="none"/>
              <path d="M6 8l6 4.5L18 8" stroke="#4caf46" stroke-width="1.2"/>
            </svg>
          </span>
          <span class="contact-text">marta.ellis@lumencell.com</span>
        </li>
        <li class="contact-row">
          <span class="contact-icon">
            <svg viewBox="0 0 24 24" fill="none" stroke="#fff" stroke-width="1.5">
              <rect x="2" y="2" width="20" height="20" rx="3"/>
              <circle cx="12" cy="12" r="5.5"/>
              <ellipse cx="12" cy="12" rx="2.4" ry="5.5"/>
              <path d="M6.5 12h11"/>
            </svg>
          </span>
          <span class="contact-text">www.lumencell.com</span>
        </li>
      </ul>
    </div>
    <div class="brand-panel">
      <div class="wordmark"><span class="dot"></span>Lumen CELL</div>
    </div>
  </section>

</body>
</html>
```